Corvane Optics PowerPoint Template

Corvane Optics needs a nice new corporate PowerPoint template, to be used for all types of presentations: sales, business development, finance, board/exec, etc.

I'd like to get a clean layout that reflects the brand (www.corvaneoptics.example), has a bright, interesting title slide, and then minimal graphics on the content slides. Ideally the content slides would have a header, "co" circle part of the Corvane Optics logo (either above or below), copyright/confidential footer, and page #.

About us: we have developed a revolutionary new array camera for mobile devices, providing depth at every pixel. Focus on any subject, change focus (even on multiple subjects) after you take the photo, capture linear measurements, scale and segment your images, change backgrounds, and apply filters, all from any device.
It's not just about megapixels anymore.
See www.corvaneoptics.example for info.

Target Market(s)

The audience for 90% of our presentations is highly educated executives at technology companies.

Industry/Entity Type

Camera

Requirements
Nice to have
• It would be great to show an image in a phone UI on the title slide, similar to the approach on our website.
Helpful to have tagline on title slide: "A smart camera for your smartphone." It may also fit on the content slides - feel free to try.
I attached a product photo, but using it is completely optional.
I'd like the "co" circle on the content slides, but the whole logo on the title slides.
Thanks!

```html
<!DOCTYPE html>
<html lang="en">
<head>
<meta charset="utf-8">
<title>Corvane Optics – Presentation Template</title>
<link href="https://fonts.googleapis.com/css2?family=Source+Sans+3:wght@300;400;600;700&family=Roboto+Condensed:wght@300;400&display=swap" rel="stylesheet">
<style>
  :root {
    --canvas: #999999;
    --slide: #ffffff;
    --navy: #0d3a56;
    --ink: #14213d;
    --text: #4a4a4a;
    --rule: #8a8a8a;
    --device: #151515;
    --screen-a: #c9a77f;
    --screen-b: #6f8c8a;
    --caption-bg: rgba(232, 214, 186, 0.9);
  }
  * { margin: 0; padding: 0; box-sizing: border-box; }
  html, body { width: 1200px; height: 900px; overflow: hidden; }
  body {
    background: var(--canvas);
    position: relative;
    font-family: "Source Sans 3", sans-serif;
  }
  .slide {
    position: absolute;
    left: 310px;
    width: 475px;
    height: 368px;
    background: var(--slide);
    overflow: hidden;
  }
  .slide--title { top: 88px; }
  .slide--content { top: 466px; }

  /* Title slide */
  .masthead {
    position: absolute; left: 29px; top: 33px;
    display: flex; align-items: center; gap: 12px;
  }
  .brand { display: flex; align-items: center; flex-shrink: 0; }
  .brand__dot { width: 20px; height: 20px; border-radius: 50%; background: var(--navy); }
  .brand__name {
    margin-left: 5px; font-weight: 700; font-size: 18px; color: var(--navy);
    letter-spacing: -0.2px; line-height: 1; white-space: nowrap;
  }
  .tagline {
    font-weight: 600; font-size: 10.5px; line-height: 11.5px; color: #333;
    white-space: nowrap;
  }
  .floor {
    position: absolute; left: 0; right: 0; top: 240px; height: 108px;
    background: linear-gradient(to bottom, rgba(220,220,220,0.2), rgba(210,210,210,0.55) 45%, rgba(235,235,235,0.3));
  }
  .device {
    position: absolute; left: 99px; top: 118px; width: 283px; height: 146px;
    border-radius: 8px; background: var(--device);
    box-shadow: 0 6px 10px rgba(0,0,0,0.25);
  }
  .device__screen {
    position: absolute; left: 36px; top: 14px; width: 204px; height: 117px;
    background: linear-gradient(120deg, var(--screen-a), var(--screen-b));
  }
  .device__caption {
    position: absolute; left: 1px; top: 74px; width: 199px; height: 16px;
    background: var(--caption-bg); border-radius: 3px;
    font-weight: 600; font-size: 10px; line-height: 16px; color: #222; padding-left: 3px;
    white-space: nowrap;
  }
  .cover-title {
    position: absolute; left: 0; right: 0; top: 298px; text-align: center;
    font-family: "Roboto Condensed", sans-serif; font-weight: 300;
    font-size: 24px; color: var(--navy); line-height: 1;
  }
  .cover-meta {
    position: absolute; left: 0; right: 0; top: 328px; text-align: center;
    font-size: 13.5px; color: #333; line-height: 1;
  }

  /* Content slide */
  .header { position: absolute; left: 28px; top: 34px; display: flex; align-items: center; }
  .header__dot { width: 21px; height: 21px; border-radius: 50%; background: var(--ink); }
  .header__title {
    margin-left: 9px; font-size: 17.5px; font-weight: 400; color: var(--ink);
    letter-spacing: -0.3px; line-height: 1;
  }
  .bullets { position: absolute; left: 88px; top: 90px; width: 308px; list-style: none; }
  .bullets li {
    position: relative; font-weight: 300; font-size: 8.8px; line-height: 16.8px;
    color: var(--text); text-align: justify; margin-bottom: 10px;
  }
  .bullets li::before {
    content: ""; position: absolute; left: -8px; top: 5px;
    width: 6px; height: 6px; border-radius: 50%; background: var(--ink);
  }
  .footer-rule {
    position: absolute; left: 19px; width: 436px; top: 341px; height: 1px; background: var(--rule);
  }
  .footer-tagline {
    position: absolute; left: 23px; top: 347px;
    font-weight: 700; font-size: 6.8px; line-height: 8px; color: #222;
  }
  .page-number { position: absolute; right: 19px; top: 346px; font-size: 6.8px; color: #444; }
</style>
</head>
<body>

<section class="slide slide--title">
  <div class="masthead">
    <div class="brand">
      <span class="brand__dot"></span>
      <span class="brand__name">Corvane Optics</span>
    </div>
    <p class="tagline">A Smart Camera<br>for Your Smartphone</p>
  </div>

  <div class="floor" role="img" aria-label="Soft grey perspective floor beneath the phone"></div>

  <div class="device" role="img" aria-label="Smartphone in landscape showing a photo of friends taking a picture together">
    <div class="device__screen">
      <p class="device__caption">Mobile array camera captures 3D video</p>
    </div>
  </div>

  <h1 class="cover-title">Lorem ipsum dolor sit amet</h1>
  <p class="cover-meta">Birmingham, March 25, 2011</p>
</section>

<section class="slide slide--content">
  <div class="header">
    <span class="header__dot"></span>
    <h2 class="header__title">PRESENTATION TITLE</h2>
  </div>

  <ul class="bullets">
    <li>Lorem ipsum dolor sit amet, consectetur adipisicing elit, sed do eiusmod tempor incididunt ut labore et dolore magna aliqua. Ut enim ad minim veniam, quis nostrud exercitation ullamco laboris nisi ut aliquip ex ea commodo consequat. Duis aute irure dolor in reprehenderit in voluptate velit esse cillum dolore eu</li>
    <li>Lorem ipsum dolor sit amet, consectetur adipisicing elit, sed do eiusmod tempor incididunt ut labore et dolore magna aliqua. Ut enim ad minim veniam, quis nostrud exercitation ullamco laboris nisi ut aliquip ex ea commodo consequat. Duis aute irure dolor in reprehenderit in voluptate velit esse cillum dolore eu</li>
    <li>Lorem ipsum dolor sit amet, consectetur adipisicing elit, sed do eiusmod tempor incididunt ut labore et dolore magna aliqua. Ut enim ad minim veniam, quis nostrud exercitation ullamco laboris nisi ut aliquip ex ea commodo consequat. Duis aute irure dolor in reprehenderit in voluptate velit esse cillum dolore eu</li>
  </ul>

  <div class="footer-rule"></div>
  <p class="footer-tagline">A Smart Camera<br>for Your Smartphone</p>
  <p class="page-number">2</p>
</section>

</body>
</html>
```